Alternative Therapy Service Needs Compelling Brochure Design

Quiet Harbor Path, LLC is looking for a brochure design that will capture the attention of others looking for support both mentally and physically. Colors that are soothing, convey support, growth, and strength are key!
The colors in my logo are great and a play or combo of any of those would be great....I am hoping the brochure can feel like an oasis from one's everyday life....I also love the tree concept of my logo as trees convey the growth and support that Quiet Harbor Path offers...I am excited to see what you can create!

Hello All Designers! I am looking for a design on the outside and inside of the brochure...tri-fold or bi-fold brochures work! Please do not be concerned with adding text from my website into it as I am adding new services and will be updating the website ASAP I would like the brochure to be editable and easy to add and delete from as I change my business and add new elements and people to my staff... Thanks for all your contribution to my brochure project!

Reason: There are many designers who were invited later in the process and I would like to give them more time to design!

```html
<!DOCTYPE html>
<html lang="en">
<head>
<meta charset="utf-8">
<title>Quiet Harbor Path – Brochure Spread</title>
<link href="https://fonts.googleapis.com/css2?family=Lato:wght@300;400;700;900&family=Ubuntu:wght@300;400;700&display=swap" rel="stylesheet">
<style>
  :root {
    --blue: #1e9ad6;
    --blue-deep: #1589cc;
    --blue-light: #4cb8ea;
    --ink: #1d1d1b;
    --grey-title: #4a4a4a;
    --paper: #ffffff;
    --sand: #cdbfa8;
    --blossom: #e6b7cf;
  }
  * { margin: 0; padding: 0; box-sizing: border-box; }
  html, body { width: 1200px; height: 782px; overflow: hidden; background: var(--paper); }
  .spread {
    position: relative; width: 1200px; height: 782px; overflow: hidden;
    background: var(--paper); font-family: "Ubuntu", sans-serif; color: var(--ink);
  }
  .hero-photo {
    position: absolute; left: 0; top: 0; width: 735px; height: 339px;
    background:
      radial-gradient(ellipse 120px 90px at 90px 90px, var(--blossom), transparent 70%),
      radial-gradient(ellipse 200px 120px at 380px 170px, #8e8a83, transparent 75%),
      radial-gradient(ellipse 90px 80px at 570px 250px, #f4f1ec, transparent 75%),
      radial-gradient(ellipse 140px 100px at 620px 40px, #efdf9c, transparent 75%),
      linear-gradient(180deg, #d9cdb8 0%, var(--sand) 60%, #bfae93 100%);
  }
  .intro-tab {
    position: absolute; left: 42px; top: 259px; width: 202px; height: 177px;
    background: var(--blue); color: var(--paper); padding: 101px 0 0 6px;
  }
  .intro-tab::after {
    content: ""; position: absolute; left: 0; right: 0; bottom: 0; height: 4px; background: var(--blue-deep);
  }
  .intro-tab .lead { font-family: "Lato", sans-serif; font-weight: 300; font-size: 21px; line-height: 1; }
  .intro-tab .title { font-family: "Lato", sans-serif; font-weight: 700; font-size: 27px; line-height: 1.3; white-space: nowrap; }

  .body-copy { font-size: 9px; line-height: 13.5px; }
  .body-copy p + p { margin-top: 13.5px; }
  .intro-copy { position: absolute; left: 42px; top: 451px; width: 448px; }
  .section-head {
    font-family: "Lato", sans-serif; font-weight: 700; color: var(--blue); font-size: 13px; line-height: 1;
  }
  .integrative-head { position: absolute; left: 42px; top: 533px; }
  .col { position: absolute; top: 547px; width: 202px; text-align: justify; }
  .col-left { left: 42px; }
  .col-right { left: 256px; }

  .profile-panel {
    position: absolute; left: 634px; top: 121px; width: 189px; height: 661px;
    border-radius: 95px 95px 0 0;
    background: linear-gradient(180deg, var(--blue-deep) 0%, var(--blue) 45%, var(--blue-light) 100%);
    color: var(--paper);
  }
  .portrait {
    position: absolute; left: 17px; top: 16px; width: 156px; height: 156px; border-radius: 50%;
    border: 3px solid var(--paper);
    background: radial-gradient(circle at 50% 45%, #c98a6a 0%, #8b5a3c 45%, #b07a5a 100%);
  }
  .profile-name { position: absolute; left: 6px; top: 212px; font-size: 11.5px; font-weight: 400; }
  .profile-copy {
    position: absolute; left: 6px; top: 228px; width: 177px;
    font-size: 8.8px; line-height: 13.6px; letter-spacing: 0.25px; text-align: justify;
  }
  .profile-copy p + p { margin-top: 13.6px; }

  .reiki-title {
    position: absolute; left: 851px; top: 128px; font-family: "Lato", sans-serif; font-weight: 300;
    font-size: 70px; line-height: 1; color: var(--grey-title);
  }
  .reiki-photo {
    position: absolute; left: 848px; top: 223px; width: 309px; height: 167px;
    background:
      radial-gradient(ellipse 80px 50px at 130px 120px, #e9c8ad, transparent 75%),
      linear-gradient(135deg, #f3f1ee 0%, #e5e1dc 55%, #d8d2cb 100%);
  }
  .reiki-photo .mark-card {
    position: absolute; right: 8px; top: 10px; width: 82px; height: 148px; background: var(--paper);
  }
  .overview-head { position: absolute; left: 849px; top: 424px; }
  .overview-copy { position: absolute; left: 849px; top: 439px; width: 310px; font-size: 9.2px; line-height: 13.7px; }
  .overview-copy p + p { margin-top: 13.7px; }
  .overview-copy .emphasis { font-weight: 700; }
</style>
</head>
<body>
<main class="spread">
  <div class="hero-photo" role="img" aria-label="Photo of a smooth grey stone engraved with the word Harmony, a white heart stone and pink lilies on sand"></div>

  <div class="intro-tab">
    <div class="lead">What is</div>
    <div class="title">SOMAVOICE?</div>
  </div>

  <section class="intro-copy body-copy">
    <p>SomaVoice is a comprehensive and dynamically designed system of energy medicine that is constantly evolving by unifying a large number of highly recognized healing methods and principles of knowledge into one all-encompassing system. SomaVoice can be used as a stand-alone system to address all physical, mental, and emotional health issues. SomaVoice can be seamlessly integrated to support any other health care modality to increase its effectiveness and promote even faster healing.</p>
  </section>

  <h2 class="section-head integrative-head">Thoroughly Integrative</h2>
  <div class="col col-left body-copy">
    <p>SomaVoice has evolved into a state-of-the-art approach to integrative healthcare by drawing upon Western medicine's scientifically supported research along with a large number of highly recognized ancient and modern healing methods and principles of knowledge.</p>
    <p>SomaVoice is non-invasive, safe, and easy to learn.</p>
    <p>SomaVoice facilitates the body/mind's well being through enhanced communication.</p>
    <p>The SomaVoice System creates an energy balance in the body that induces the body's own innate</p>
  </div>
  <div class="col col-right body-copy">
    <p>restorative powers, thus it does not diagnose, nor address disease symptomatically.</p>
    <p>From layperson to medical specialist, SomaVoice has several levels of application that meet the needs of those who wish to help themselves and/or others regain and retain a healthier balance within body, mind, and spirit.</p>
    <p>The revolutionary application of practical, effective techniques is what sets the SomaVoice System apart.</p>
  </div>

  <aside class="profile-panel">
    <div class="portrait" role="img" aria-label="Portrait photo of the practitioner"></div>
    <h3 class="profile-name">Dana Whitlow, CPB, RM</h3>
    <div class="profile-copy">
      <p>Learning, living, and sharing The SomaVoice System is my passion! Since my certification as a SomaVoice practitioner in 2004, I have seen and experienced things nothing short of miraculous.</p>
      <p>On a personal note, I've experienced improvements in my physical, mental, and emotional health. Before SomaVoice I experienced weekly migraine headaches, fatigue, and bouts of depression. Today, I am free of weekly migraines. Migraines are a rare occurrence and if and when they surface I have some SomaVoice techniques that can clear them in about an hour. In addition, I am experiencing a new level of health. I have boundless energy and a renewed sense of who I really am. The SomaVoice System has helped me to peel away the layers of false beliefs I had about myself and my world. This stripping away process for me has created a level of Freedom in my life that I could of only dreamed about. I am honored and grateful to be a part of such an amazing system.</p>
      <p>I strongly encourage you to come and explore what The SomaVoice System can do for you!</p>
    </div>
  </aside>

  <h1 class="reiki-title">Reiki</h1>
  <div class="reiki-photo" role="img" aria-label="Photo of a hand held above a relaxed woman receiving a Reiki treatment">
    <div class="mark-card" role="img" aria-label="Card with the Reiki characters in brush lettering"></div>
  </div>

  <h2 class="section-head overview-head">A Brief Overview</h2>
  <div class="overview-copy">
    <p>Reiki is a Japanese technique for stress reduction and relaxation that also promotes healing. It is administered by "laying on hands" and is based on the idea that an unseen "life force energy" flows through us and is what causes us to be alive. If one's "life force energy" is low, then we are more likely to get sick or feel stress, and if it is high, we are more capable of being happy and healthy.</p>
    <p>The word Reiki is made of two Japanese words – Rei which means "God's Wisdom or the Higher Power" and Ki which is "life force energy". So Reiki is actually "spiritually guided life force energy."</p>
    <p>A treatment feels like a wonderful glowing radiance that flows through and around you. Reiki treats the whole person including body, emotions, mind and spirit creating many beneficial effects that include relaxation and feelings of peace, security and wellbeing. Many have reported miraculous results.</p>
    <p class="emphasis">Reiki is a simple, natural and safe method of spiritual healing and self-improvement that everyone can use. It has been effective in helping virtually every known illness and malady and always creates a beneficial effect. It also works in conjunction with all other medical or therapeutic techniques to relieve side effects and promote recovery.</p>
  </div>
</main>
</body>
</html>
```